1. Can you describe what your company does?
-> We at M and P Orbex, we do Tube bending and its subassemblies. We can cater to different materials like Mild Steel, Stainless Steel, Aluminium and other non-ferrous material. We collaborate with our clients to make precise components to meet their industry requirements. At M&P Orbex we cater to smaller batches or high-volume requirements as per project needs.

2. Who are your target customers for the website?
-> Automotive, Road construction, warehouse equipment, Data centers, beverage equipment industry, electronics products manufacturers for making fixtures.
-> customers which require tubes and pipe bending, exhaust pipes, sheet metal parts

3. Do you have an existing domain name / website address?
-> This was an existing site: https://www.mandporbex.co.in/industry
-> using design.com I created this: https://sitelaunch.web/MandPOrbexpvtltd
But I am not very satisfied with the one I have created using design.com

4. In addition to a Home Page, which other pages / sections would you like your website to have:
About Us
Contact Us
Products / Services
Office / Mailing Address
Terms and Conditions

For each of the pages / sections you’d like to have, please provide the text (and images, if available) you would like to include.
-> Can you use the content that I have added on design.com : https://sitelaunch.web/MandPOrbexpvtltd

5. Which of the below are features and functionalities your website will need:
Image Gallery
Videos
Contact Form

6. Please provide the URLs for the social media profiles you'd like to link to the website.
-> Don't have one yet.

Coding

Coded - Design and coding required

```html
<!DOCTYPE html>
<html lang="en">
<head>
<meta charset="UTF-8">
<title>M and P Orbex — Industries We Serve</title>
<link rel="stylesheet" href="https://fonts.googleapis.com/css2?family=Mulish:wght@500;600;700&family=Arimo:wght@400;700&display=swap">
<style>
  :root{
    --band-dark:#1f0072;
    --section:#42288f;
    --white:#ffffff;
    --nav-active:#3f6fd6;
    --logo-ink:#1f3f8a;
    --auto-tone:linear-gradient(160deg,#c9a27a 0%,#7a5a48 55%,#3a3230 100%);
    --road-tone:linear-gradient(180deg,#4d8be0 0%,#d9e3ee 40%,#d7a22a 65%,#7b5a34 100%);
    --ware-tone:linear-gradient(160deg,#bfbab0 0%,#e1c21c 50%,#3b3a36 100%);
  }
  *{box-sizing:border-box;margin:0;padding:0}
  html,body{width:1200px;height:981px;overflow:hidden;background:var(--section)}
  .page{position:relative;width:1200px;height:981px}
  .masthead{position:absolute;left:0;top:0;width:1200px;height:210px;background:var(--band-dark)}
  .brand-badge{position:absolute;left:8px;top:18px;width:71px;height:72px;background:var(--white);
    display:flex;align-items:flex-end;justify-content:center;padding-bottom:8px;
    font-family:"Arimo",sans-serif;font-size:7px;color:var(--logo-ink)}
  .brand-name{position:absolute;left:91px;top:38px;font-family:"Arimo",sans-serif;font-weight:700;
    font-size:26px;color:var(--white)}
  .main-nav{position:absolute;top:20px;left:0;width:1200px;font-family:"Arimo",sans-serif;font-size:14px;color:var(--white)}
  .main-nav a{position:absolute;color:inherit;text-decoration:none;letter-spacing:.3px}
  .main-nav a.is-active{color:var(--nav-active)}
  .chapter{position:absolute;left:95px;top:100px;width:213px;height:100px}
  .chapter-rule{position:absolute;left:0;top:44px;width:213px;height:8px;background:var(--white)}
  .chapter-num{position:absolute;left:62px;top:0;font-family:"Arimo",sans-serif;font-weight:700;
    font-size:86px;line-height:100px;color:var(--white)}
  .industries{position:absolute;left:0;top:210px;width:1200px;height:736px;background:var(--section);font-family:"Mulish",sans-serif;color:var(--white)}
  .industries h1{position:absolute;left:0;top:68px;width:1160px;text-align:center;font-weight:600;font-size:48px}
  .industry{position:absolute;top:228px;width:247px}
  .industry-photo{display:block;margin:0 auto;border-radius:50%}
  .industry h2{position:absolute;top:140px;left:-40px;width:327px;text-align:center;font-size:18px;font-weight:600}
  .industry p{position:absolute;top:198px;left:0;width:247px;font-size:13.6px;font-weight:600;line-height:25.6px;text-align:justify}
  .footer-band{position:absolute;left:0;top:946px;width:1200px;height:35px;background:var(--band-dark)}
</style>
</head>
<body>
<div class="page">
  <header class="masthead">
    <div class="brand-badge">M and P Orbex</div>
    <div class="brand-name">M and P Orbex</div>
    <nav class="main-nav">
      <a style="left:608px">Home</a>
      <a style="left:692px">Services</a>
      <a class="is-active" style="left:795px">Industry</a>
      <a style="left:894px">Products</a>
      <a style="left:998px">About Us</a>
      <a style="left:1105px">Contact Us</a>
    </nav>
    <div class="chapter">
      <div class="chapter-rule"></div>
      <div class="chapter-num">02</div>
    </div>
  </header>

  <section class="industries">
    <h1>Industries We Serve</h1>

    <article class="industry" style="left:170px">
      <div class="industry-photo" role="img" aria-label="Riders on scooters on a city street" style="width:126px;height:126px;background:var(--auto-tone)"></div>
      <h2>Automotive</h2>
      <p>We specialize in the manufacturing of high-quality exhaust pipes, muffler, handlebars, cross bars, swing arms, air intake pipes for automobiles. We are proud to offer a wide range of products that will meet your every need and exceed your expectations. Contact us today to learn more about our products and services.</p>
    </article>

    <article class="industry" style="left:471px">
      <div class="industry-photo" role="img" aria-label="Yellow crawler bulldozer under a cloudy sky" style="width:126px;height:126px;background:var(--road-tone)"></div>
      <h2>Road Construction</h2>
      <p>We understand the importance of reliable and top-quality products for road construction projects.<br>That's why we are dedicated to providing the most advanced manufacturing solutions for exhaust pipes, mufflers, and railing systems, as well as partnering with road construction companies to offer the highest quality products available.</p>
    </article>

    <article class="industry" style="left:771px">
      <div class="industry-photo" role="img" aria-label="Yellow forklift in a warehouse aisle" style="width:106px;height:106px;margin-top:2px;background:var(--ware-tone)"></div>
      <h2>Warehousing Equipment</h2>
      <p style="top:197px">Reliability and durability are key when it comes to Warehousing Equipment. That's why we offer a wide range of high-quality chassis and driver cabins, exhaust pipes, mufflers, air intake pipes to accommodate your specific requirements.</p>
    </article>
  </section>

  <div class="footer-band"></div>
</div>
</body>
</html>
```